Marketing material for IT Company
Brochure/Sales Sheet/Flyer
Brochure will be in two languages, and tri-fold. Would go like this; front (outer) side: first fold: page for information in 2nd languge, second fold: page for information in 2nd language, third fold: cover page in 1st language; back side (inner) side: first fold is for information in 1st language, second fold is for information in 1st language, third fold is cover page for 2nd language.
Information Technology
Brochure view and dimensions are in an uploaded file. Size of flyer equals to size of 1 fold of brochure (i.e one brochure size = 3 flyers size). Size of Sales Sheet is equal to brochure's size. (Sales Sheet won't be folded).
Trifold Brochure view and dimensions
Tulmori logo and Divisions logos (CMYK)
Tulmori logo and Divisions logos (PMS)
Tulmori vertical logo and Divisions vertical logos (CMYK)
Tulmori vertical logo and Divisions vertical logos (PMS)
Tulmori old Brochure (uploaded as an example)
Example of our folder, if it can help
Example of our biz card, if it can help
To help you understand how we see our brochure, one more PIC
Tulmori logo colors information

```html
<!DOCTYPE html>
<html lang="en">
<head>
<meta charset="utf-8">
<title>Tulmori – Flyers and Tri-fold Brochure</title>
<link rel="stylesheet" href="https://fonts.googleapis.com/css2?family=Open+Sans:wght@400;600;700&display=swap">
<style>
  :root {
    --yellow: #f4b400;
    --red: #e5402a;
    --green: #67b33d;
    --blue: #1f87c8;
    --ink: #2f4654;
    --text: #5b6670;
    --paper: #ffffff;
    --footer: #e9ecef;
    --stage: #f1f2f4;
    --photo-a: #c9d3dc;
    --photo-b: #8796a3;
  }
  * { box-sizing: border-box; margin: 0; padding: 0; }
  html, body { width: 1200px; height: 763px; overflow: hidden; }
  body {
    background: var(--stage);
    font-family: "Open Sans", Arial, sans-serif;
    color: var(--text);
    position: relative;
  }

  /* ---------- flyer ---------- */
  .flyer {
    position: absolute;
    width: 144px;
    height: 341px;
    background: var(--paper);
    box-shadow: 0 2px 6px rgba(0,0,0,.18);
    overflow: hidden;
  }
  .flyer.yellow { --accent: var(--yellow); }
  .flyer.red    { --accent: var(--red); }
  .flyer.green  { --accent: var(--green); }
  .flyer.blue   { --accent: var(--blue); }

  .brand {
    display: flex;
    align-items: center;
    gap: 4px;
    font-weight: 700;
    color: var(--ink);
    letter-spacing: .2px;
  }
  .brand .dot { border-radius: 50%; background: var(--accent); flex: none; }

  .flyer-header { height: 36px; display: flex; align-items: center; justify-content: center; }
  .flyer-header .brand { font-size: 13px; }
  .flyer-header .dot { width: 12px; height: 12px; }

  .flyer-photo { position: relative; height: 104px; }
  .flyer-photo .image {
    position: absolute; inset: 0;
    background: linear-gradient(160deg, var(--photo-a), var(--photo-b));
  }
  .flyer-photo svg { position: absolute; left: 0; width: 100%; }
  .flyer-photo .swoosh-top { top: -1px; height: 22px; }
  .flyer-photo .swoosh-bottom { bottom: -1px; height: 28px; }

  .division { display: flex; align-items: center; gap: 4px; padding: 8px 10px 4px; }
  .division .brand { font-size: 8px; }
  .division .dot { width: 7px; height: 7px; }
  .division .unit { font-size: 5px; color: var(--accent); font-weight: 600; margin-left: -2px; margin-top: 6px; }

  .flyer-body { padding: 2px 10px; font-size: 4.6px; line-height: 1.45; }
  .flyer-body p { margin-bottom: 4px; }
  .flyer-body ul { list-style: none; }
  .flyer-body li { position: relative; padding-left: 6px; margin-bottom: 3px; }
  .flyer-body li::before {
    content: ""; position: absolute; left: 0; top: 1.6px;
    width: 3px; height: 3px; background: var(--accent);
  }

  .flyer-footer {
    position: absolute; left: 0; right: 0; bottom: 0; height: 12px;
    background: var(--footer);
    border-top: 2px solid var(--accent);
    font-size: 5px; letter-spacing: 1.4px; text-align: center; line-height: 10px;
    color: var(--ink);
  }

  /* ---------- brochure ---------- */
  .brochure {
    position: absolute;
    width: 524px;
    height: 341px;
    background: var(--paper);
    box-shadow: 0 2px 6px rgba(0,0,0,.18);
    overflow: hidden;
  }
  .panel-head {
    position: absolute; top: 0; height: 96px; width: 175px;
    padding: 8px 10px; color: #fff; font-size: 4.6px; line-height: 1.45;
  }
  .panel-head.blue { left: 0; background: var(--blue); }
  .panel-head.green { left: 175px; background: var(--green); }
  .panel-head .brand { color: #fff; font-size: 8px; margin-bottom: 5px; }
  .panel-head .dot { width: 7px; height: 7px; background: #fff; }
  .panel-head ul { list-style: none; margin-top: 4px; }
  .panel-head li { padding-left: 5px; position: relative; margin-bottom: 2px; }
  .panel-head li::before { content: ""; position: absolute; left: 0; top: 1.6px; width: 2.5px; height: 2.5px; background: #fff; }

  .panel-photo {
    position: absolute; left: 0; top: 96px; width: 350px; height: 110px;
    background: linear-gradient(100deg, #b7c3cd, #e5e9ec 55%, #9eacb8);
  }
  .brochure svg.wave { position: absolute; left: 0; top: 178px; width: 350px; height: 40px; }

  .panel-foot {
    position: absolute; top: 212px; width: 175px; height: 115px;
    padding: 10px; color: #fff; font-size: 4.6px; line-height: 1.45;
  }
  .panel-foot.yellow { left: 0; background: var(--yellow); }
  .panel-foot.red { left: 175px; background: var(--red); }
  .panel-foot .brand { color: #fff; font-size: 8px; margin-bottom: 5px; }
  .panel-foot .dot { width: 7px; height: 7px; background: #fff; }
  .panel-foot p { margin-bottom: 4px; }

  .brochure-footer {
    position: absolute; left: 0; width: 350px; bottom: 0; height: 14px;
    background: var(--footer); font-size: 5px; letter-spacing: 1.4px;
    line-height: 14px; text-align: right; padding-right: 12px; color: var(--ink);
  }

  .cover { position: absolute; left: 350px; top: 0; width: 174px; height: 341px; }
  .cover-logo { height: 120px; display: flex; align-items: center; justify-content: center; }
  .cover-logo .brand { flex-direction: column; gap: 6px; font-size: 22px; }
  .cover-logo .dot { width: 42px; height: 42px; background: var(--red); }
  .cover-photo {
    position: absolute; left: 0; right: 0; top: 120px; bottom: 0;
    background: linear-gradient(170deg, #d3dbe2, #7f8f9c);
  }
  .cover svg { position: absolute; left: 0; top: 108px; width: 174px; height: 30px; }
</style>
</head>
<body>

<!-- Flyers, first row -->
<article class="flyer yellow" style="left:24px; top:24px;">
  <header class="flyer-header"><div class="brand"><span class="dot"></span>tulmori</div></header>
  <div class="flyer-photo">
    <div class="image" role="img" aria-label="Photo of a support team wearing headsets"></div>
    <svg class="swoosh-bottom" viewBox="0 0 144 28" preserveAspectRatio="none"><path d="M0 10 Q72 -6 144 18 L144 28 L0 28 Z" fill="var(--accent)"/><path d="M0 18 Q72 4 144 24 L144 28 L0 28 Z" fill="#fff"/></svg>
  </div>
  <div class="division"><div class="brand"><span class="dot"></span>tulmori</div><span class="unit">systems</span></div>
  <div class="flyer-body">
    <p>We design, build and support reliable information systems that help growing companies work faster, safer and smarter every single day.</p>
    <ul><li>Network design and secure cloud hosting</li><li>Custom software for daily business tasks</li><li>Round the clock support from our team</li></ul>
  </div>
  <footer class="flyer-footer">www.lorvexnet.com</footer>
</article>

<article class="flyer yellow" style="left:180px; top:24px;">
  <header class="flyer-header"><div class="brand"><span class="dot"></span>tulmori</div></header>
  <div class="flyer-photo">
    <div class="image" role="img" aria-label="Photo of a support team wearing headsets"></div>
    <svg class="swoosh-bottom" viewBox="0 0 144 28" preserveAspectRatio="none"><path d="M0 10 Q72 -6 144 18 L144 28 L0 28 Z" fill="var(--accent)"/><path d="M0 18 Q72 4 144 24 L144 28 L0 28 Z" fill="#fff"/></svg>
  </div>
  <div class="division"><div class="brand"><span class="dot"></span>tulmori</div><span class="unit">systems</span></div>
  <div class="flyer-body">
    <p>We design, build and support reliable information systems that help growing companies work faster, safer and smarter every single day.</p>
    <ul><li>Network design and secure cloud hosting</li><li>Custom software for daily business tasks</li><li>Round the clock support from our team</li></ul>
  </div>
  <footer class="flyer-footer">www.lorvexnet.com</footer>
</article>

<article class="flyer red" style="left:336px; top:24px;">
  <header class="flyer-header"><div class="brand"><span class="dot"></span>tulmori</div></header>
  <div class="flyer-photo">
    <div class="image" role="img" aria-label="Photo of a businessman working at a laptop"></div>
    <svg class="swoosh-bottom" viewBox="0 0 144 28" preserveAspectRatio="none"><path d="M0 18 Q72 -4 144 8 L144 28 L0 28 Z" fill="var(--accent)"/><path d="M0 24 Q72 6 144 16 L144 28 L0 28 Z" fill="#fff"/></svg>
  </div>
  <div class="division"><div class="brand"><span class="dot"></span>tulmori</div><span class="unit">sport</span></div>
  <div class="flyer-body">
    <p>We design, build and support reliable information systems that help growing companies work faster, safer and smarter every single day.</p>
    <ul><li>Network design and secure cloud hosting</li><li>Custom software for daily business tasks</li><li>Round the clock support from our team</li></ul>
  </div>
  <footer class="flyer-footer">www.lorvexnet.com</footer>
</article>

<article class="flyer red" style="left:492px; top:24px;">
  <header class="flyer-header"><div class="brand"><span class="dot"></span>tulmori</div></header>
  <div class="flyer-photo">
    <div class="image" role="img" aria-label="Photo of a businessman working at a laptop"></div>
    <svg class="swoosh-bottom" viewBox="0 0 144 28" preserveAspectRatio="none"><path d="M0 18 Q72 -4 144 8 L144 28 L0 28 Z" fill="var(--accent)"/><path d="M0 24 Q72 6 144 16 L144 28 L0 28 Z" fill="#fff"/></svg>
  </div>
  <div class="division"><div class="brand"><span class="dot"></span>tulmori</div><span class="unit">sport</span></div>
  <div class="flyer-body">
    <p>We design, build and support reliable information systems that help growing companies work faster, safer and smarter every single day.</p>
    <ul><li>Network design and secure cloud hosting</li><li>Custom software for daily business tasks</li><li>Round the clock support from our team</li></ul>
  </div>
  <footer class="flyer-footer">www.lorvexnet.com</footer>
</article>

<!-- Flyers, second row -->
<article class="flyer green" style="left:24px; top:398px;">
  <header class="flyer-header"><div class="brand"><span class="dot"></span>tulmori</div></header>
  <div class="flyer-photo">
    <div class="image" role="img" aria-label="Photo of a group of smiling office staff"></div>
    <svg class="swoosh-bottom" viewBox="0 0 144 28" preserveAspectRatio="none"><path d="M0 8 Q72 -4 144 20 L144 28 L0 28 Z" fill="var(--accent)"/><path d="M0 16 Q72 6 144 25 L144 28 L0 28 Z" fill="#fff"/></svg>
  </div>
  <div class="division"><div class="brand"><span class="dot"></span>tulmori</div><span class="unit">services</span></div>
  <div class="flyer-body">
    <p>We design, build and support reliable information systems that help growing companies work faster, safer and smarter every single day.</p>
    <ul><li>Network design and secure cloud hosting</li><li>Custom software for daily business tasks</li><li>Round the clock support from our team</li></ul>
  </div>
  <footer class="flyer-footer">www.lorvexnet.com</footer>
</article>

<article class="flyer green" style="left:180px; top:398px;">
  <header class="flyer-header"><div class="brand"><span class="dot"></span>tulmori</div></header>
  <div class="flyer-photo">
    <div class="image" role="img" aria-label="Photo of a group of smiling office staff"></div>
    <svg class="swoosh-bottom" viewBox="0 0 144 28" preserveAspectRatio="none"><path d="M0 8 Q72 -4 144 20 L144 28 L0 28 Z" fill="var(--accent)"/><path d="M0 16 Q72 6 144 25 L144 28 L0 28 Z" fill="#fff"/></svg>
  </div>
  <div class="division"><div class="brand"><span class="dot"></span>tulmori</div><span class="unit">services</span></div>
  <div class="flyer-body">
    <p>We design, build and support reliable information systems that help growing companies work faster, safer and smarter every single day.</p>
    <ul><li>Network design and secure cloud hosting</li><li>Custom software for daily business tasks</li><li>Round the clock support from our team</li></ul>
  </div>
  <footer class="flyer-footer">www.lorvexnet.com</footer>
</article>

<article class="flyer blue" style="left:336px; top:398px;">
  <header class="flyer-header"><div class="brand"><span class="dot"></span>tulmori</div></header>
  <div class="flyer-photo">
    <div class="image" role="img" aria-label="Photo of a businessman seated at a desk"></div>
    <svg class="swoosh-top" viewBox="0 0 144 22" preserveAspectRatio="none"><path d="M0 0 L144 0 L144 6 Q72 22 0 4 Z" fill="#fff"/></svg>
    <svg class="swoosh-bottom" viewBox="0 0 144 28" preserveAspectRatio="none"><path d="M0 20 Q72 -2 144 10 L144 28 L0 28 Z" fill="var(--accent)"/><path d="M0 25 Q72 8 144 18 L144 28 L0 28 Z" fill="#fff"/></svg>
  </div>
  <div class="division"><div class="brand"><span class="dot"></span>tulmori</div><span class="unit">solutions</span></div>
  <div class="flyer-body">
    <p>We design, build and support reliable information systems that help growing companies work faster, safer and smarter every single day.</p>
    <ul><li>Network design and secure cloud hosting</li><li>Custom software for daily business tasks</li><li>Round the clock support from our team</li></ul>
  </div>
  <footer class="flyer-footer">www.lorvexnet.com</footer>
</article>

<article class="flyer blue" style="left:492px; top:398px;">
  <header class="flyer-header"><div class="brand"><span class="dot"></span>tulmori</div></header>
  <div class="flyer-photo">
    <div class="image" role="img" aria-label="Photo of a businessman seated at a desk"></div>
    <svg class="swoosh-top" viewBox="0 0 144 22" preserveAspectRatio="none"><path d="M0 0 L144 0 L144 6 Q72 22 0 4 Z" fill="#fff"/></svg>
    <svg class="swoosh-bottom" viewBox="0 0 144 28" preserveAspectRatio="none"><path d="M0 20 Q72 -2 144 10 L144 28 L0 28 Z" fill="var(--accent)"/><path d="M0 25 Q72 8 144 18 L144 28 L0 28 Z" fill="#fff"/></svg>
  </div>
  <div class="division"><div class="brand"><span class="dot"></span>tulmori</div><span class="unit">solutions</span></div>
  <div class="flyer-body">
    <p>We design, build and support reliable information systems that help growing companies work faster, safer and smarter every single day.</p>
    <ul><li>Network design and secure cloud hosting</li><li>Custom software for daily business tasks</li><li>Round the clock support from our team</li></ul>
  </div>
  <footer class="flyer-footer">www.lorvexnet.com</footer>
</article>

<!-- Tri-fold brochures -->
<section class="brochure" style="left:652px; top:24px;">
  <div class="panel-head blue">
    <div class="brand"><span class="dot"></span>tulmori</div>
    <p>Our engineers plan, deliver and maintain complete IT services for offices of every size.</p>
    <ul><li>Server and network setup</li><li>Data backup and recovery</li></ul>
  </div>
  <div class="panel-head green">
    <div class="brand"><span class="dot"></span>tulmori</div>
    <p>Our engineers plan, deliver and maintain complete IT services for offices of every size.</p>
    <ul><li>Business software licences</li><li>Staff training and guidance</li></ul>
  </div>
  <div class="panel-photo" role="img" aria-label="Photo of a smiling businessman in a modern office lobby"></div>
  <svg class="wave" viewBox="0 0 350 40" preserveAspectRatio="none"><path d="M0 34 Q175 0 350 22 L350 40 L0 40 Z" fill="#7d8790"/></svg>
  <div class="panel-foot yellow">
    <div class="brand"><span class="dot"></span>tulmori</div>
    <p>Our engineers plan, deliver and maintain complete IT services for offices of every size.</p>
  </div>
  <div class="panel-foot red">
    <div class="brand"><span class="dot"></span>tulmori</div>
    <p>Our engineers plan, deliver and maintain complete IT services for offices of every size.</p>
  </div>
  <footer class="brochure-footer">www.lorvexnet.com</footer>
  <div class="cover">
    <div class="cover-logo"><div class="brand"><span class="dot"></span>tulmori</div></div>
    <div class="cover-photo" role="img" aria-label="Photo of a businessman touching a glowing digital screen"></div>
    <svg viewBox="0 0 174 30" preserveAspectRatio="none"><path d="M0 0 L174 0 L174 10 Q87 34 0 14 Z" fill="#fff"/></svg>
  </div>
</section>

<section class="brochure" style="left:652px; top:398px;">
  <div class="panel-head blue">
    <div class="brand"><span class="dot"></span>tulmori</div>
    <p>Our engineers plan, deliver and maintain complete IT services for offices of every size.</p>
    <ul><li>Server and network setup</li><li>Data backup and recovery</li></ul>
  </div>
  <div class="panel-head green">
    <div class="brand"><span class="dot"></span>tulmori</div>
    <p>Our engineers plan, deliver and maintain complete IT services for offices of every size.</p>
    <ul><li>Business software licences</li><li>Staff training and guidance</li></ul>
  </div>
  <div class="panel-photo" role="img" aria-label="Photo of a smiling businessman in a modern office lobby"></div>
  <svg class="wave" viewBox="0 0 350 40" preserveAspectRatio="none"><path d="M0 34 Q175 0 350 22 L350 40 L0 40 Z" fill="#7d8790"/></svg>
  <div class="panel-foot yellow">
    <div class="brand"><span class="dot"></span>tulmori</div>
    <p>Our engineers plan, deliver and maintain complete IT services for offices of every size.</p>
  </div>
  <div class="panel-foot red">
    <div class="brand"><span class="dot"></span>tulmori</div>
    <p>Our engineers plan, deliver and maintain complete IT services for offices of every size.</p>
  </div>
  <footer class="brochure-footer">www.lorvexnet.com</footer>
  <div class="cover">
    <div class="cover-logo"><div class="brand"><span class="dot"></span>tulmori</div></div>
    <div class="cover-photo" role="img" aria-label="Photo of a businessman touching a glowing digital screen"></div>
    <svg viewBox="0 0 174 30" preserveAspectRatio="none"><path d="M0 0 L174 0 L174 10 Q87 34 0 14 Z" fill="#fff"/></svg>
  </div>
</section>

</body>
</html>
```